An internal sign in a physiotherapy clinic with gym. About working hard

We are a physiotherapy clinic / gym and we are wanting an internal wall to be a large sign with a great slogan
We are after 3 parts to it
1. The image / backdrop
2. The slogan
3. Our clinic logo

I have attached some images of the concept of what we are after. It can be climbing a mountain, rockclimbing and even hard work in a gym.

The slogan is:
"IF IT DOESN'T CHALLENGE YOU, IT WON'T CHANGE YOU"

Logo
I have attached a few different versions of our logo to assist you in the sign based on the background

THE SIGN SIZE WILL BE:
2935mm wide x 1885mm high

```html
<!DOCTYPE html>
<html lang="en">
<head>
<meta charset="utf-8">
<title>If It Doesn't Challenge You, It Won't Change You</title>
<link rel="stylesheet" href="https://fonts.googleapis.com/css2?family=Oswald:wght@700&display=swap">
<style>
  :root {
    --paper: #ffffff;
    --navy: #1b2150;
    --sky: #4bb8e0;
    --photo-climber-a: #b88a6e;
    --photo-climber-b: #2f3f5c;
    --photo-gym-a: #8c7466;
    --photo-gym-b: #1c1c20;
  }
  * { margin: 0; padding: 0; box-sizing: border-box; }
  html, body {
    width: 1200px;
    height: 771px;
    overflow: hidden;
    background: var(--paper);
  }
  .wall-sign {
    position: relative;
    width: 1200px;
    height: 771px;
    background: var(--paper);
    font-family: "Oswald", "Arial Narrow", sans-serif;
  }
  .photo {
    position: absolute;
    opacity: 0.85;
  }
  .photo--climber {
    left: 0;
    top: 0;
    width: 350px;
    height: 412px;
    background: linear-gradient(160deg, var(--photo-climber-a) 0%, var(--photo-climber-a) 30%, var(--photo-climber-b) 75%);
    clip-path: polygon(0 0, 100% 0, 100% 285px, 245px 285px, 245px 100%, 0 100%);
  }
  .photo--lifter {
    left: 997px;
    top: 309px;
    width: 203px;
    height: 440px;
    border-radius: 40px 0 0 40px;
    background: linear-gradient(180deg, var(--photo-gym-a) 0%, var(--photo-gym-b) 45%, var(--photo-gym-b) 100%);
  }
  .slogan {
    position: absolute;
    left: 273px;
    top: 304px;
    text-transform: uppercase;
    font-weight: 700;
    line-height: 1;
  }
  .slogan__line {
    display: block;
    white-space: nowrap;
  }
  .slogan__line--challenge {
    color: var(--navy);
    font-size: 56px;
    letter-spacing: 0.3px;
  }
  .slogan__line--change {
    color: var(--sky);
    font-size: 75px;
    letter-spacing: 0.5px;
    margin-top: 10px;
  }
  .clinic-mark {
    position: absolute;
    left: 352px;
    top: 648px;
    display: flex;
    align-items: center;
    gap: 16px;
  }
  .clinic-mark__dot {
    width: 46px;
    height: 46px;
    border-radius: 50%;
    background: var(--sky);
  }
  .clinic-mark__name {
    color: var(--navy);
    font-weight: 700;
    font-size: 40px;
    text-transform: uppercase;
    line-height: 1;
  }
</style>
</head>
<body>
  <main class="wall-sign">
    <div class="photo photo--climber" role="img" aria-label="Photo of a shirtless rock climber in jeans abseiling on a rope with harness and gear"></div>
    <div class="photo photo--lifter" role="img" aria-label="Photo of a woman in black gym wear bending forward doing dumbbell rows"></div>

    <h1 class="slogan">
      <span class="slogan__line slogan__line--challenge">If it doesn’t challenge you,</span>
      <span class="slogan__line slogan__line--change">It won’t change you</span>
    </h1>

    <div class="clinic-mark">
      <span class="clinic-mark__dot"></span>
      <span class="clinic-mark__name">Larkfield Sports Medicine</span>
    </div>
  </main>
</body>
</html>
```